Vantaglorification - Short Film Poster

Link to Film: https://clipvessel.example/482915006/kq7730ab2

Links to BTS photos:

https://filecrate.example/folders/8XpQm2LtRz4VbNw7JkYh3DsGa6EcFu0Po?share=on

https://filecrate.example/folders/5Tn_R8wKcLpZ2bJdXq9MhY4VeAoSf7iGu?share=on

We need to design a poster for a student short film produced at the Harrowmere Screen Academy. I can provide a link to the film for you to watch and pull stills from in needed. W also have many BTS photos that could be useful. The film's palette features yellow most heavily. The film is about a young man who tries to learn to hypnotize or "vantaglorify" someone into going on a date with him, only to find out that his mentor is a con man.

Target Market(s)

Ages 18-29

Industry/Entity Type

Film

Colors

Designer to choose colors to be used in the design.

Requirements
Must have
• Needs to include HSA Conservatory logo in bottom right corner.
Nice to have
• You'll notice our film is set in a donut shop. We’d like for donuts to be the featured element of the poster. I'm thinking the poster could be a bunch of donuts being sucked down into a hypnotic swirl with Reuben, the younger man, at the center of it. Another idea could be something from the donut spinning on the counter at the 00:58 mark of the film. You can film the link to the film in the project description.
Should not have
• Avoid harsh lines and angles.

```html
<!DOCTYPE html>
<html lang="en">
<head>
<meta charset="utf-8">
<title>Vantaglorification – Poster</title>
<link rel="stylesheet" href="https://fonts.googleapis.com/css2?family=Antonio:wght@400;600&family=Archivo+Black&display=swap">
<style>
  :root {
    --ink-black: #050505;
    --shirt-navy: #0f1a2e;
    --skin: #c99a84;
    --citrus: #f08a12;
    --citrus-deep: #c8650a;
    --title-white: #f1f1ef;
    --title-red: #b5122b;
    --credit-white: #e9e9e9;
  }
  html, body {
    margin: 0;
    padding: 0;
    width: 810px;
    height: 1200px;
    overflow: hidden;
    background: var(--ink-black);
  }
  .poster {
    position: relative;
    width: 810px;
    height: 1200px;
    overflow: hidden;
    background: var(--ink-black);
  }
  .poster__photo {
    position: absolute;
    inset: 0;
    background:
      radial-gradient(ellipse 235px 235px at 400px 745px, var(--citrus) 0%, var(--citrus) 78%, var(--citrus-deep) 96%, rgba(200,101,10,0) 100%),
      radial-gradient(ellipse 330px 300px at 400px 760px, rgba(201,154,132,0.85) 0%, rgba(201,154,132,0.55) 70%, rgba(201,154,132,0) 100%),
      linear-gradient(180deg, var(--shirt-navy) 0%, #121d33 45%, #0b0f18 70%, var(--ink-black) 88%);
  }
  .poster__title {
    position: absolute;
    left: 0;
    top: 0;
    width: 810px;
    height: 300px;
  }
  .poster__title text {
    font-family: "Archivo Black", "Arial Black", sans-serif;
    font-size: 58px;
    letter-spacing: 1px;
  }
  .title__shadow { fill: var(--title-red); }
  .title__face { fill: var(--title-white); }
  .credits {
    position: absolute;
    left: 30px;
    top: 1090px;
    width: 580px;
    font-family: "Antonio", "Arial Narrow", sans-serif;
    color: var(--credit-white);
    text-transform: uppercase;
    line-height: 1;
  }
  .credits__line {
    display: flex;
    justify-content: center;
    align-items: baseline;
    gap: 5px;
    white-space: nowrap;
    margin-bottom: 9px;
  }
  .credits__label { font-size: 8px; font-weight: 400; letter-spacing: 0.2px; }
  .credits__name { font-size: 14px; font-weight: 400; letter-spacing: 0.3px; margin-right: 4px; }
  .school-mark {
    position: absolute;
    left: 650px;
    top: 1110px;
    width: 125px;
    display: flex;
    align-items: center;
    gap: 7px;
    font-family: "Antonio", "Arial Narrow", sans-serif;
    font-weight: 600;
    font-size: 16px;
    line-height: 1;
    white-space: nowrap;
    color: var(--credit-white);
    text-transform: uppercase;
  }
  .school-mark__square {
    width: 11px;
    height: 11px;
    background: var(--credit-white);
    flex: none;
  }
</style>
</head>
<body>
<main class="poster">
  <div class="poster__photo" role="img" aria-label="Photograph: two cupped hands holding a large orange citrus fruit in front of a navy shirt on a dark background"></div>

  <svg class="poster__title" viewBox="0 0 810 300" aria-label="Vantaglorification">
    <defs>
      <path id="title-arc" d="M 45 245 Q 405 -65 770 245"/>
      <path id="title-arc-shadow" d="M 45 251 Q 405 -59 770 251"/>
    </defs>
    <text class="title__shadow" text-anchor="middle"><textPath href="#title-arc-shadow" startOffset="50%">VANTAGLORIFICATION</textPath></text>
    <text class="title__face" text-anchor="middle"><textPath href="#title-arc" startOffset="50%">VANTAGLORIFICATION</textPath></text>
  </svg>

  <section class="credits">
    <div class="credits__line">
      <span class="credits__label">HSA Conservatory presents</span>
      <span class="credits__name">Vantaglorification</span>
      <span class="credits__label">starring</span>
      <span class="credits__name">Ezra Holloway</span>
      <span class="credits__name">Marisa Quennell</span>
      <span class="credits__name">Sal Ravenna</span>
      <span class="credits__name">Dana R. Whitlock</span>
    </div>
    <div class="credits__line">
      <span class="credits__label">music by</span>
      <span class="credits__name">Tobias Okonra</span>
      <span class="credits__label">edited by</span>
      <span class="credits__name">Wen Ada Lu</span>
      <span class="credits__label">production design by</span>
      <span class="credits__name">Greta Ashfield</span>
    </div>
    <div class="credits__line">
      <span class="credits__label">cinematography by</span>
      <span class="credits__name">Colin Abner Westover</span>
      <span class="credits__label">produced by</span>
      <span class="credits__name">Rove</span>
      <span class="credits__label">written and directed by</span>
      <span class="credits__name">Nolan Perrywick</span>
    </div>
  </section>

  <div class="school-mark">
    <span class="school-mark__square"></span>
    <span class="school-mark__name">HSA Conservatory</span>
  </div>
</main>
</body>
</html>
```